Card design for orthopaedic surgeons working as The Brindlewood Orthopaedic Centre

Business cards, letterhead

Colors

Designer to choose colors to be used in the design.

Requirements
Must have
• Late addition.
• Cards letterhead must have logos of
• Corvane Federated Institute of Surgeons
• Meridale Orthopaedic Society
Nice to have
• Back of card to have space for appointment time to be added by hand and some blank space for writing incidental other notes.

```html
<!DOCTYPE html>
<html lang="en">
<head>
<meta charset="utf-8">
<title>The Brindlewood Orthopaedic Centre – Business Card</title>
<link href="https://fonts.googleapis.com/css2?family=Lato:wght@400;700&display=swap" rel="stylesheet">
<style>
  :root{
    --backdrop:#d6d6d6;
    --navy:#022d46;
    --sky:#4fa9e1;
    --white:#ffffff;
    --card-shadow:0 6px 22px rgba(0,0,0,.35);
  }
  html,body{margin:0;padding:0;overflow:hidden;}
  body{width:1000px;height:1200px;background:var(--backdrop);position:relative;font-family:'Lato',sans-serif;}
  .card{position:absolute;border-radius:22px;overflow:hidden;box-shadow:var(--card-shadow);}
  .card--front{left:110px;top:120px;width:778px;height:446px;background:var(--white);}
  .card--back{left:110px;top:633px;width:780px;height:447px;background:var(--navy);}
  .card__wave{position:absolute;left:0;top:0;width:100%;height:100%;}
  .brand-name{position:absolute;margin:0;font-family:'Lato',sans-serif;font-weight:400;white-space:nowrap;letter-spacing:-0.3px;}
  .card--front .brand-name{right:36px;top:78px;font-size:30px;color:var(--navy);}
  .card--back .brand-name{left:0;right:0;text-align:center;top:222px;font-size:42px;color:var(--white);}
  .contact{position:absolute;left:40px;top:218px;color:var(--white);}
  .contact__name{margin:0;font-size:22px;font-weight:700;color:var(--sky);letter-spacing:.3px;line-height:26px;}
  .contact__role{margin:2px 0 0;font-size:18px;line-height:22px;}
  .contact__address{margin:14px 0 0;font-size:17.5px;line-height:25px;}
  .contact__list{list-style:none;margin:12px 0 0;padding:0;font-size:17.5px;line-height:25px;}
  .contact__list li{display:flex;align-items:center;gap:10px;}
  .contact__icon{width:16px;height:16px;flex:none;}
</style>
</head>
<body>

<section class="card card--front" aria-label="Front of business card">
  <svg class="card__wave" viewBox="0 0 778 446" aria-hidden="true">
    <path d="M0,140 C220,138 340,210 440,268 C540,326 620,348 778,332" fill="none" stroke="var(--sky)" stroke-width="9"/>
    <path d="M0,154 C220,152 340,222 440,280 C540,338 620,360 778,336 L778,446 L0,446 Z" fill="var(--navy)"/>
  </svg>
  <p class="brand-name">The Brindlewood Orthopaedic Centre</p>
  <div class="contact">
    <h1 class="contact__name">ROWAN ELLERY</h1>
    <p class="contact__role">Owner</p>
    <p class="contact__address">4120 Larkfield Road, Ashbourne Vale<br>NC 2, United States</p>
    <ul class="contact__list">
      <li><svg class="contact__icon" viewBox="0 0 16 16"><path d="M3.2 1.5l2.4 2.6-1.3 2a9 9 0 0 0 5.6 5.6l2-1.3 2.6 2.4-1.6 2A12 12 0 0 1 1.2 3.1z" fill="var(--sky)"/></svg>000-000-000-000</li>
      <li><svg class="contact__icon" viewBox="0 0 16 16"><rect x="1" y="3.5" width="14" height="9" fill="var(--sky)"/><path d="M1 3.5l7 5.5 7-5.5" fill="none" stroke="var(--navy)" stroke-width="1.2"/></svg>info@websitename.com</li>
      <li><svg class="contact__icon" viewBox="0 0 16 16" fill="none" stroke="var(--sky)" stroke-width="1.2"><circle cx="8" cy="8" r="6.5"/><ellipse cx="8" cy="8" rx="2.8" ry="6.5"/><path d="M1.5 8h13M2.5 4.8h11M2.5 11.2h11"/></svg>www.websitename.com</li>
    </ul>
  </div>
</section>

<section class="card card--back" aria-label="Back of business card">
  <p class="brand-name">The Brindlewood Orthopaedic Centre</p>
</section>

</body>
</html>
```